Re-design of Business Card

We require a design for our business card.

Quorin is a supplier of industrial packaging specializing in plastic products. We are undergoing a rebranding to appear more corporate. We have changed our company name to quorin and have a new logo.

I have uploaded our old card design with the previous company name.
Don't copy the current design. We are looking for a new design.

Industry/Entity Type

Manufacturing

Contact Information for Business Card

please don't copy the current design. we are looking for a new design.

Font styles to use
Sans Serif

Colors

Designer to choose colors to be used in the design.

Requirements
Must have
• clean and easy to read.

```html
<!DOCTYPE html>
<html lang="en">
<head>
<meta charset="utf-8">
<title>Quorin Business Card</title>
<link rel="stylesheet" href="https://fonts.googleapis.com/css2?family=Open+Sans:wght@400;700;800&display=swap">
<style>
  :root {
    --backdrop: #e4e4e4;
    --card: #2f3032;
    --accent: #f47b20;
    --text-light: #f2f2f2;
    --emboss: #3a3b3e;
  }
  * { box-sizing: border-box; margin: 0; padding: 0; }
  html, body {
    width: 1200px; height: 1125px; overflow: hidden;
    background: var(--backdrop);
    font-family: "Open Sans", Arial, sans-serif;
  }
  .stage { position: relative; width: 1200px; height: 1125px; }
  .card {
    position: absolute; left: 180px; width: 840px; height: 480px;
    background: var(--card);
    border-bottom: 9px solid var(--accent);
    box-shadow: 0 10px 24px rgba(0,0,0,0.25);
  }
  .card--front { top: 50px; }
  .card--back { top: 590px; }

  .front-name {
    position: absolute; inset: 0;
    display: flex; align-items: center; justify-content: center;
    font-weight: 800; font-size: 96px; letter-spacing: 2px;
    color: var(--emboss);
  }

  .back-brand {
    position: absolute; left: 50px; top: 0; height: 471px; width: 360px;
    display: flex; align-items: center; justify-content: center; gap: 16px;
    font-weight: 800; font-size: 72px; color: var(--accent);
  }
  .back-brand .brand-square { width: 26px; height: 26px; background: var(--accent); }

  .divider {
    position: absolute; left: 440px; top: 45px; width: 2px; height: 380px;
    background: var(--accent);
  }
  .details { position: absolute; left: 470px; top: 45px; width: 350px; color: var(--text-light); }
  .person-name { font-weight: 700; font-size: 27px; color: var(--accent); letter-spacing: 1px; line-height: 1.1; }
  .person-title { font-size: 19px; margin-top: 2px; }
  .address { font-size: 19px; line-height: 1.3; margin-top: 26px; }
  .contacts { list-style: none; margin-top: 30px; }
  .contacts li { display: flex; align-items: center; gap: 10px; font-size: 21px; line-height: 1.3; }
  .contacts svg { width: 18px; height: 18px; fill: var(--accent); flex: none; }
</style>
</head>
<body>
<main class="stage">
  <section class="card card--front" aria-label="Card front">
    <div class="front-name">QUORIN</div>
  </section>

  <section class="card card--back" aria-label="Card back">
    <div class="back-brand"><span class="brand-square"></span>QUORIN</div>
    <div class="divider"></div>
    <div class="details">
      <p class="person-name">DANA WHITLOCK</p>
      <p class="person-title">Machinery Sales Manager</p>
      <p class="address">48 Harbour St, Riverglen<br>Qld, 4120 Australia</p>
      <ul class="contacts">
        <li><svg viewBox="0 0 24 24"><path d="M6.6 10.8a15 15 0 0 0 6.6 6.6l2.2-2.2a1 1 0 0 1 1-.25 11 11 0 0 0 3.6.6 1 1 0 0 1 1 1V20a1 1 0 0 1-1 1A17 17 0 0 1 3 4a1 1 0 0 1 1-1h3.5a1 1 0 0 1 1 1 11 11 0 0 0 .6 3.6 1 1 0 0 1-.25 1z"/></svg>1300 555 014</li>
        <li><svg viewBox="0 0 24 24"><path d="M7 1h10a2 2 0 0 1 2 2v18a2 2 0 0 1-2 2H7a2 2 0 0 1-2-2V3a2 2 0 0 1 2-2zm0 3v14h10V4zm5 15.5a1 1 0 1 0 0 2 1 1 0 0 0 0-2z"/></svg>+61 7 5550 1234</li>
        <li><svg viewBox="0 0 24 24"><path d="M6 2h12v5H6zM4 8h16a2 2 0 0 1 2 2v7h-4v5H6v-5H2v-7a2 2 0 0 1 2-2zm4 8v4h8v-4z"/></svg>1300 555 014</li>
        <li><svg viewBox="0 0 24 24"><path d="M2 5h20v2l-10 6L2 7zm0 4.3l10 6 10-6V19H2z"/></svg>dana@quorin.com.au</li>
        <li><svg viewBox="0 0 24 24"><circle cx="12" cy="12" r="10"/></svg>www.quorin.com.au</li>
      </ul>
    </div>
  </section>
</main>
</body>
</html>
```